TernQuay Business Cards

Create business cards for our exciting new software company. We provide cloud billing systems and provisioning software for campany that need monthly SaaS and Cloud Billing

Target Market(s)

Enterprise businesses, b2b, telecom carriers, software manufactures

Industry/Entity Type

Software

```html
<!DOCTYPE html>
<html lang="en">
<head>
<meta charset="utf-8">
<title>TernQuay Business Cards</title>
<link rel="stylesheet" href="https://fonts.googleapis.com/css2?family=Jost:wght@400;500&display=swap">
<style>
  :root {
    --backdrop: #3a3a3c;
    --card-front: #1f3553;
    --card-back: #213f62;
    --accent: #72bde0;
    --ink: #e8eef5;
    --ink-soft: #c3d0de;
  }
  * { margin: 0; padding: 0; box-sizing: border-box; }
  html, body { width: 1200px; height: 900px; overflow: hidden; }
  body {
    position: relative;
    background: var(--backdrop);
    font-family: "Jost", "Futura", sans-serif;
  }
  .card {
    position: absolute;
    top: 300px;
    width: 525px;
    height: 300px;
    border-radius: 22px;
    box-shadow: 0 6px 18px rgba(0,0,0,0.35);
  }
  .card-front { left: 58px; background: var(--card-front); }
  .card-back { left: 618px; background: var(--card-back); }

  .brand {
    position: absolute;
    text-align: right;
  }
  .brand-name {
    display: flex;
    align-items: center;
    justify-content: flex-end;
    gap: 8px;
    color: var(--accent);
    font-weight: 500;
    line-height: 1;
  }
  .brand-dot {
    border-radius: 50%;
    background: var(--accent);
  }
  .brand-tagline {
    color: var(--ink-soft);
    text-transform: uppercase;
    letter-spacing: 0.06em;
    line-height: 1.25;
    margin-top: 5px;
  }

  .card-front .brand { right: 48px; top: 210px; }
  .card-front .brand-name { font-size: 30px; }
  .card-front .brand-dot { width: 12px; height: 12px; }
  .card-front .brand-tagline { font-size: 6.5px; }
  .card-front .site {
    position: absolute;
    right: 48px;
    top: 270px;
    color: var(--ink-soft);
    font-size: 9px;
    letter-spacing: 0.62em;
    margin-right: -0.62em;
  }

  .card-back .brand { right: 48px; top: 150px; }
  .card-back .brand-name { font-size: 24px; }
  .card-back .brand-dot { width: 10px; height: 10px; }
  .card-back .brand-tagline { font-size: 5.5px; }

  .contact {
    position: absolute;
    right: 48px;
    top: 203px;
    text-align: right;
    color: var(--ink);
    text-transform: uppercase;
    letter-spacing: 0.06em;
  }
  .contact-name { font-size: 14px; line-height: 1.1; }
  .contact-role { font-size: 11px; line-height: 1.2; }
  .contact-lines { margin-top: 12px; font-size: 12.5px; line-height: 1.05; }
  .contact-lines .label { color: var(--accent); }
  .contact-site { margin-top: 9px; font-size: 12.5px; }
</style>
</head>
<body>
  <section class="card card-front">
    <div class="brand">
      <div class="brand-name"><span class="brand-dot"></span>TernQuay</div>
      <div class="brand-tagline">Cloud billing and<br>operational support systems</div>
    </div>
    <div class="site">www.ternquay.com</div>
  </section>

  <section class="card card-back">
    <div class="brand">
      <div class="brand-name"><span class="brand-dot"></span>TernQuay</div>
      <div class="brand-tagline">Cloud billing and<br>operational support systems</div>
    </div>
    <div class="contact">
      <div class="contact-name">Marissa Calloway</div>
      <div class="contact-role">Manager</div>
      <div class="contact-lines">
        <div><span class="label">P:</span> 555-014-2270 <span class="label">F:</span> 555-014-7391</div>
        <div><span class="label">E:</span> info@ternquay.com</div>
      </div>
      <div class="contact-site">www.ternquay.com</div>
    </div>
  </section>
</body>
</html>
```